Brent's Custom Signs and Woodworking Business Card

I run a small business that does custom woodworking and sign making. I have a logo already that I am very fond of, and would like to continue with the theme of the logo. I'd like a business card that adds onto that theme/design and stands out among typical business cards. As you'll be able to see from the logo, we're a patriotic brand and that is paramount to us.
Contact Information for Business Card
beneath the Brent's logo, I'd like it to say
"Custom Signs & Woodworking"
Also, I'd like the following information template present on the card, preferably with the logos of instagram and facebook present besides the title.
(Name)                                 (Instragram)
(Email)                                  (Facebook)
(Phone)                                 (Website)
I would like for the name, email, and phone number to be editable so that I can have my employees utilize this card design as well. but for my card, my information is as follows
Tom "Brent" Kellerby, CEO                                           @BrentsCrafted
Tom@BrentsCrafted.example                                          Brent's Crafted
(555) 014-2273                                                         BrentsCrafted.example
As for the back side, either a full american flag, or something that catches the eye, designer's preference I suppose.
Font styles to use
Other font styles liked:
- Funkydori, an adobe typekit font. it is the same as used for the logo. I'm not sure how the whole card will look with that, so if it doesn't look right please use something that complements the script style of the logo

```html
<!DOCTYPE html>
<html lang="en">
<head>
<meta charset="utf-8">
<title>Brent's Custom Signs and Woodworking – Business Card</title>
<link rel="stylesheet" href="https://fonts.googleapis.com/css2?family=Tinos:wght@400;700&family=Lato:wght@400;700&display=swap">
<style>
  :root {
    --navy: #232f6b;
    --red: #c0202e;
    --white: #ffffff;
    --ink: #222222;
    --map-grey: #e4e4e4;
    --stage: #2a2b2f;
  }
  * { box-sizing: border-box; margin: 0; padding: 0; }
  html, body { width: 1200px; height: 800px; overflow: hidden; }
  body {
    background: var(--stage);
    display: flex;
    align-items: center;
    justify-content: center;
    gap: 40px;
    font-family: "Lato", sans-serif;
  }
  .card {
    position: relative;
    width: 540px;
    height: 309px;
    background: var(--white);
    overflow: hidden;
    box-shadow: 0 10px 30px rgba(0,0,0,.45);
  }

  /* Front side */
  .world-map {
    position: absolute;
    left: 110px; top: 40px;
    width: 380px; height: 210px;
    background: radial-gradient(ellipse at 50% 50%, var(--map-grey) 0%, rgba(228,228,228,.6) 55%, rgba(255,255,255,0) 75%);
  }
  .front .brand {
    position: absolute;
    left: 0; right: 0; top: 96px;
    text-align: center;
  }
  .brand-name {
    font-family: "Tinos", serif;
    font-weight: 700;
    color: var(--navy);
    font-size: 58px;
    line-height: 1;
  }
  .brand-tagline {
    font-family: "Lato", sans-serif;
    color: var(--ink);
    font-size: 13px;
    margin-top: 6px;
  }
  .front .website {
    position: absolute;
    left: 0; right: 0; top: 222px;
    text-align: center;
    font-family: "Tinos", serif;
    font-size: 12px;
    letter-spacing: 7px;
    color: var(--ink);
  }

  /* Back side */
  .flag-photo {
    position: absolute;
    left: 0; top: 0;
    width: 300px; height: 200px;
    background:
      linear-gradient(90deg, rgba(255,255,255,0) 55%, var(--white) 100%),
      linear-gradient(180deg, rgba(255,255,255,0) 60%, var(--white) 100%),
      linear-gradient(115deg, var(--navy) 0%, var(--navy) 45%, #e9e9ee 58%, var(--red) 72%, #f2f2f2 88%);
  }
  .back .brand {
    position: absolute;
    right: 28px; top: 26px;
    text-align: center;
  }
  .back .brand-name { font-size: 54px; }
  .rule {
    position: absolute;
    height: 1px;
    background: var(--red);
  }
  .rule-top { left: 300px; right: 20px; top: 128px; }
  .rule-name { left: 24px; right: 20px; top: 182px; }
  .holder {
    position: absolute;
    left: 30px; top: 138px;
    font-family: "Tinos", serif;
    color: var(--navy);
  }
  .holder-name { font-size: 19px; font-weight: 700; line-height: 1.1; }
  .holder-title { font-size: 13px; color: var(--ink); }
  .contact-band {
    position: absolute;
    left: 0; right: 0; top: 192px;
    height: 90px;
    background: var(--navy);
    display: flex;
    justify-content: space-between;
    align-items: center;
    padding: 0 26px 0 34px;
  }
  .red-stripe {
    position: absolute;
    left: 0; right: 0; bottom: 0;
    height: 22px;
    background: var(--red);
    border-top: 3px solid var(--white);
  }
  .contact-list { list-style: none; }
  .contact-list li {
    display: flex;
    align-items: center;
    gap: 8px;
    font-family: "Tinos", serif;
    font-size: 13px;
    color: var(--white);
    line-height: 1.8;
  }
  .icon {
    width: 16px; height: 16px;
    flex: none;
  }
</style>
</head>
<body>

  <section class="card front" aria-label="Business card front">
    <div class="world-map" role="img" aria-label="Faint grey world map behind the logo"></div>
    <div class="brand">
      <div class="brand-name">Brent's</div>
      <div class="brand-tagline">Custom Signs &amp; Woodworking</div>
    </div>
    <div class="website">BrentsCrafted.example</div>
  </section>

  <section class="card back" aria-label="Business card back">
    <div class="flag-photo" role="img" aria-label="Waving American flag photograph, stars on blue and red and white stripes"></div>

    <div class="brand">
      <div class="brand-name">Brent's</div>
      <div class="brand-tagline">Custom Signs &amp; Woodworking</div>
    </div>

    <div class="rule rule-top"></div>

    <div class="holder">
      <div class="holder-name">Tom "Brent" Kellerby</div>
      <div class="holder-title">CEO</div>
    </div>
    <div class="rule rule-name"></div>

    <div class="contact-band">
      <ul class="contact-list">
        <li>
          <svg class="icon" viewBox="0 0 16 16" aria-hidden="true">
            <circle cx="8" cy="8" r="7.3" fill="none" stroke="#fff" stroke-width="1.2"/>
            <path d="M5.2 4.6c.4-.3.9-.3 1.1.1l.7 1.3c.2.4 0 .7-.3 1l-.4.3c.4.9 1.1 1.6 2 2l.3-.4c.3-.3.6-.5 1-.3l1.3.7c.4.2.4.7.1 1.1-.6.7-1.3.9-2.1.6-1.8-.7-3.3-2.2-4-4-.3-.8-.1-1.6.3-2.4z" fill="#fff"/>
          </svg>
          (555) 014-2273
        </li>
        <li>
          <svg class="icon" viewBox="0 0 16 16" aria-hidden="true">
            <circle cx="8" cy="8" r="7.3" fill="none" stroke="#fff" stroke-width="1.2"/>
            <rect x="4" y="5.3" width="8" height="5.6" rx=".6" fill="none" stroke="#fff" stroke-width="1"/>
            <path d="M4.2 5.6L8 8.6l3.8-3" fill="none" stroke="#fff" stroke-width="1"/>
          </svg>
          Tom@BrentsCrafted.example
        </li>
      </ul>
      <ul class="contact-list">
        <li>
          <svg class="icon" viewBox="0 0 16 16" aria-hidden="true"><circle cx="8" cy="8" r="7.3" fill="none" stroke="#fff" stroke-width="1.2"/></svg>
          @BrentsCrafted
        </li>
        <li>
          <svg class="icon" viewBox="0 0 16 16" aria-hidden="true"><circle cx="8" cy="8" r="7.3" fill="none" stroke="#fff" stroke-width="1.2"/></svg>
          Brent's Crafted
        </li>
      </ul>
    </div>
    <div class="red-stripe"></div>
  </section>

</body>
</html>
```